Flyer-Design für Auto-Abo
Zielgruppe
Wir bieten ein Auto-Abo an für Privatkunden, aber auch für Unternehmen. Für Unternehmen bieten wir das gesamte Flottenmanagement an, von der Beschaffung über die Finanzierung.
Aufgabenstellung
Der Flyer soll auf A3 gedruckt werden, dann in der Mitte fefaltet werden, so dass es schlussendlich ein A4-Faltblatt ist mit 4 Seiten. Das Design soll sich an der Website anlehnen: www.velmoro.ch, www.velmoro.ch/flotte, www.velmoro.ch/business
Farben:
dunkel #284854 R40 G72 B84
hell #31CCB0 R49 G204 B176
Text Body Catamaran Regular 400
Textfarbe #284854 R40 G72 B84

```html
<!DOCTYPE html>
<html lang="de">
<head>
<meta charset="utf-8">
<title>Velmoro Faltblatt</title>
<link href="https://fonts.googleapis.com/css2?family=Catamaran:wght@300;400;500;700&display=swap" rel="stylesheet">
<style>
:root{
  --dark:#284854;
  --teal:#31CCB0;
  --band:#5cc8b3;
  --panel:#ebe8e6;
  --bg:#dcdcdc;
  --white:#ffffff;
}
*{box-sizing:border-box;margin:0;padding:0}
html,body{width:895px;height:1200px;overflow:hidden;background:var(--bg);font-family:'Catamaran',sans-serif;color:var(--dark)}
.spread{position:absolute;left:37px;width:820px;height:580px;display:flex;box-shadow:0 6px 18px rgba(0,0,0,.18)}
.spread--outside{top:13px}
.spread--inside{top:607px}
.page{position:relative;width:410px;height:580px;background:var(--white);overflow:hidden}
.page + .page{border-left:1px solid #e2e2e2}
.brand{position:absolute;left:0;right:0;text-align:center;display:flex;justify-content:center;align-items:baseline;gap:6px}
.brand__name{font-weight:700;font-size:17px;letter-spacing:1px;color:var(--dark)}
.brand__dot{width:7px;height:7px;border-radius:50%;background:var(--teal);align-self:center}
.brand__section{font-size:14px;font-weight:400;color:var(--dark)}
.photo{position:absolute}
.panel{position:absolute;background:var(--panel);padding:8px 10px}
.panel h3{font-weight:400;color:var(--teal);font-size:11px;line-height:1.15;margin:7px 0 4px}
.panel h3:first-child{margin-top:2px}
.panel p{font-size:6.3px;line-height:1.38;margin-bottom:4px}
.panel p strong{font-weight:700}
.benefits{position:absolute;left:0;right:0;bottom:0;background:var(--band);color:var(--white);padding:10px 30px}
.benefits h4{font-weight:400;font-size:11px;margin-bottom:6px}
.benefits li{list-style:none;font-size:6.3px;line-height:1.35;position:relative;padding-left:15px}
.benefits li::before{content:"";position:absolute;left:0;top:2px;width:5px;height:5px;background:var(--white)}
.headline{position:absolute;left:0;right:0;text-align:center;font-size:15px;font-weight:400}
/* cover */
.cover__photo{left:0;top:0;width:410px;height:296px}
.cover__brand{top:26px;flex-direction:column;align-items:center;gap:0}
.cover__brand .brand__name{font-size:24px}
.cover__tag{font-size:7px}
.cover__title{position:absolute;top:78px;left:0;right:0;text-align:center;font-size:22px;font-weight:400;line-height:1.2}
.cover__band{position:absolute;top:296px;left:0;right:0;height:36px;background:var(--band);color:var(--white);font-size:13px;padding:9px 23px}
.pillars{position:absolute;top:350px;left:23px;right:28px;display:flex;gap:14px}
.pillar{flex:1}
.pillar h5{font-size:10px;font-weight:400;margin-bottom:4px}
.pillar p{background:var(--panel);font-size:7.3px;line-height:1.4;padding:5px 4px}
.cover__badge{position:absolute;top:472px;left:118px;right:28px;background:var(--band);color:var(--white);font-size:8.5px;padding:7px 8px}
.cover__note{position:absolute;top:519px;left:23px;right:28px;font-size:7px;color:var(--teal);line-height:1.4}
.cover__url{position:absolute;top:547px;left:0;right:0;text-align:center;font-size:12px}
</style>
</head>
<body>

<section class="spread spread--outside">
  <div class="page page--community">
    <div class="brand" style="top:22px"><span class="brand__dot"></span><span class="brand__name">VELMORO</span><span class="brand__section">Community</span></div>
    <svg class="photo" style="left:0;top:60px" width="180" height="124" role="img" aria-label="Hand hält Smartphone vor einem Elektroauto"><defs><linearGradient id="p1" x1="0" y1="0" x2="1" y2="1"><stop offset="0" stop-color="#5d6f7c"/><stop offset=".6" stop-color="#b9a69a"/><stop offset="1" stop-color="#8d2f3c"/></linearGradient></defs><rect width="180" height="124" fill="url(#p1)"/></svg>
    <svg class="photo" style="left:0;top:192px" width="180" height="124" role="img" aria-label="Elektroauto auf einer Wiese vor verschneitem Berg"><defs><linearGradient id="p2" x1="0" y1="0" x2="0" y2="1"><stop offset="0" stop-color="#8fb3d8"/><stop offset=".45" stop-color="#d9dde2"/><stop offset="1" stop-color="#4f7a2f"/></linearGradient></defs><rect width="180" height="124" fill="url(#p2)"/></svg>
    <svg class="photo" style="left:0;top:325px" width="180" height="123" role="img" aria-label="Elektroauto vor einem alten Steinhaus"><defs><linearGradient id="p3" x1="0" y1="0" x2="1" y2="1"><stop offset="0" stop-color="#6f8d4a"/><stop offset=".5" stop-color="#c2b8a8"/><stop offset="1" stop-color="#6a5040"/></linearGradient></defs><rect width="180" height="123" fill="url(#p3)"/></svg>
    <div class="panel" style="left:190px;top:54px;width:210px;height:401px">
      <h3>Die perfekte Lösung für<br>deine Liegenschaft</h3>
      <p>Immer mehr neue Bauvorhaben werden nach den Vorgaben der 2000-Watt Gesellschaft gebaut. Das bedeutet, dass nicht mehr für jede Wohnung ein Parkplatz zur Verfügung gestellt wird. Stattdessen ist es Aufgabe des Vermieters, eine Mobilitätslösung anzubieten, die von den Bewohnern genutzt werden kann. Hier bieten sich vor allem E-Autos an.</p>
      <p>Im Abo enthalten sind alle Kosten: Steuern, Versicherungen (Vollkasko mit 1000.- Selbstbehalt bei Kollision), Gebühren, Winterräder inkl. Lagerung und Montage, alle erforderlichen Services und Reparaturen.</p>
      <h3>Mit Velmoro bist du flexibel und<br>bekommst alles aus einer Hand</h3>
      <p>Das Sharing übernimmt unser Partner Carlio. Und zur Mietermanagementplattform Hausnetz besteht beispielsweise bereits eine Integration.</p>
      <p>Du definierst selbst, wer wann und zu welchen Konditionen Zugriff auf das Fahrzeug hat. So könnten deine Mitarbeitenden beispielsweise gratis fahren, deine Anwohner zu Vorzugskonditionen und externe Mieter zu einem etwas höheren Preis. In Kooperation mit der Voltrix bieten wir Ladeinfrastruktur an. Und selbst Reinigung und Unterhalt des Fahrzeuges können wir übernehmen.</p>
      <h3>Unsere Flottenmanager sind für dich<br>da – 365 Tage rund um die Uhr</h3>
      <p>Velmoro ist die perfekte Lösung für Überbauungen, Business Parks oder touristische Einrichtungen. Auf Wunsch erhältst du das Fahrzeug mit deinem Logo beklebt für mehr Visibilität.</p>
    </div>
    <div class="benefits" style="height:125px">
      <h4>Deine Vorteile auf einen Blick:</h4>
      <ul>
        <li>Transparenz – du weisst, was dich das Auto im Monat kostet. Alles was noch dazu kommt ist Strom.</li>
        <li>Unsere erfahrenen Flottenmanager sind dein direkter Kontakt und kümmern sich um alles. Auch Schadenfälle werden durch sie erledigt.</li>
        <li>Sicherheit – du verfügst über einen Premium-Versicherungsschutz der Solvara</li>
        <li>Solvara ist mit 1.1 Millionen versicherter Fahrzeuge ein etablierter Player im Markt</li>
        <li>Du profitierst von unserem Service-/Pannen und Reparaturnetzwerk</li>
      </ul>
    </div>
  </div>

  <div class="page page--cover">
    <svg class="photo cover__photo" width="410" height="296" role="img" aria-label="Kleines weisses Elektroauto auf einer Strasse in der Abendsonne"><defs><linearGradient id="pc" x1="0" y1="0" x2="0" y2="1"><stop offset="0" stop-color="#dfe2e6"/><stop offset=".55" stop-color="#c9bfb2"/><stop offset=".7" stop-color="#8f8779"/><stop offset="1" stop-color="#4d4f52"/></linearGradient></defs><rect width="410" height="296" fill="url(#pc)"/></svg>
    <div class="brand cover__brand"><span class="brand__name">VELMORO</span><span class="cover__tag">Das Auto-Abo der Solvara</span></div>
    <h1 class="cover__title">Die Alternative zu<br>Autokauf und Leasing</h1>
    <div class="cover__band">Mit Velmoro fährst du zu einem monatlichen Abo-Preis.</div>
    <div class="pillars">
      <div class="pillar"><h5>Transparenz</h5><p>Du weisst, was dich das Auto im Monat kostet.<br><br>Alles was noch dazu kommt ist Tanken und Strom.</p></div>
      <div class="pillar"><h5>Flexibilität</h5><p>Wenn sich dein Leben ändert, kannst du dein Velmoro Abo anpassen.</p></div>
      <div class="pillar"><h5>Sicherheit</h5><p>Unsere Fahrzeugexperten sind rund um die Uhr für dich da, auch im Ausland.</p></div>
      <div class="pillar"><h5>Sharing</h5><p>Teile dein Auto mit Dritten, ganz ohne Probleme und ohne Sorgen.</p></div>
    </div>
    <div class="cover__badge">Inklusive Premium-Versicherungsschutz der Solvara</div>
    <p class="cover__note">Du bist mindestens 21 Jahre, hast den Wohnsitz in der Schweiz und Liechtenstein und verfügst über einen gültigen Führerausweis? Dann kannst du Velmoro benutzen.</p>
    <div class="cover__url">www.velmoro.ch</div>
  </div>
</section>

<section class="spread spread--inside">
  <div class="page page--abo">
    <div class="brand" style="top:22px"><span class="brand__dot"></span><span class="brand__name">VELMORO</span><span class="brand__section">Abo</span></div>
    <div class="headline" style="top:50px">Autofahren ohne den ganzen Papierkram</div>
    <div class="panel" style="left:22px;top:82px;width:176px;height:318px">
      <h3>Das Auto im Abo</h3>
      <p>Bis anhin konntest du ein Auto entweder kaufen, finanzieren oder leasen. Jetzt bietet dir Velmoro eine bessere und bequemere Variante: das Auto im Abo.</p>
      <p>Du zahlst einen festen Betrag im Monat. Darin enthalten sind alle Steuern, Versicherungen (Vollkasko mit CHF 1000.- Selbstbehalt bei Kollision), Gebühren, Winterräder inklusive Lagerung und Montage und alle erforderlichen Services und Reparaturen. Ausserdem haben wir dir eine Verkehrsrechtschutzversicherung dazu gepackt.</p>
      <p>Und das Beste: du bleibst flexibel. Ändert sich dein Leben, passt sich Velmoro deinen Bedürfnissen an. Du brauchst ein kleineres/grösseres Fahrzeug – oder keines mehr? Kein Problem!</p>
      <p><strong>Im Winter ein 4x4 SUV, im Sommer ein Cabrio, probiere das mal mit deinem Leasing-Vertrag!</strong></p>
      <p>Du findest in unserem Webshop alle verfügbaren Fahrzeuge.</p>
    </div>
    <div class="panel" style="left:210px;top:82px;width:178px;height:318px">
      <h3>Der Abschluss ist rein online</h3>
      <p>Wir brauchen nur deine Adresse und ein Foto deines Führerausweises. Du musst dann nur noch entscheiden, ob du die erste Zahlung per Kreditkarte oder Rechnung vornehmen willst. Das war auch schon alles. Kein Papierkram, keine Unterschriften – alles so einfach, als würdest du online ein paar Schuhe kaufen.</p>
      <p><strong>Du bist mindestens 21 Jahre, hast den Wohnsitz in der Schweiz und Liechtenstein und verfügst über einen gültigen Führerausweis (Lernfahrausweis gilt leider nicht)? Dann kannst du Velmoro benutzen.</strong></p>
      <p>Da du im Fahrzeugausweis stehst, kannst du einen Anwohnerparkausweis beantragen und bekommst auch am Zoll keine Probleme, wenn du ins Ausland willst.</p>
      <p>Und: du kannst dein Auto jederzeit mit anderen teilen und musst dir keine Sorgen machen, im Schadenfall auf Kosten sitzen zu bleiben.</p>
      <p>Unsere Fahrzeugexperten sind 365 Tage rund um die Uhr für dich da, auch aus dem Ausland.</p>
    </div>
    <svg class="photo" style="left:0;top:412px" width="410" height="168" role="img" aria-label="Mann sitzt auf einer schwarzen Limousine vor einem Stadthaus"><defs><linearGradient id="pa" x1="0" y1="0" x2="0" y2="1"><stop offset="0" stop-color="#b7b2aa"/><stop offset=".5" stop-color="#6f6a64"/><stop offset="1" stop-color="#9e9994"/></linearGradient></defs><rect width="410" height="168" fill="url(#pa)"/><text x="380" y="150" text-anchor="end" fill="#ffffff" font-family="Catamaran, sans-serif" font-size="12">www.velmoro.ch</text></svg>
  </div>

  <div class="page page--flotte">
    <div class="brand" style="top:22px"><span class="brand__dot"></span><span class="brand__name">VELMORO</span><span class="brand__section">Flotte</span></div>
    <div class="headline" style="top:50px">Rundum sorglos und aus einer Hand</div>
    <svg class="photo" style="left:0;top:80px" width="410" height="160" role="img" aria-label="Reihe geparkter Fahrzeuge einer Firmenflotte"><defs><linearGradient id="pf" x1="0" y1="0" x2="1" y2="1"><stop offset="0" stop-color="#3a3d42"/><stop offset=".5" stop-color="#9ea2a6"/><stop offset="1" stop-color="#d5d8db"/></linearGradient></defs><rect width="410" height="160" fill="url(#pf)"/></svg>
    <div class="panel" style="left:22px;top:252px;width:178px;height:200px">
      <h3>Deine Fahrzeugflotte in guten Händen, egal ob 3 oder 300</h3>
      <p>Eine Fahrzeugflotte immer mobil zu halten, kann für ein KMU eine ganz schöne Herausforderung sein. Fahrzeuge müssen beschafft werden, Leasingverträge werden abgeschlossen. Und dann sind da noch Steuern, Versicherungen, Gebühren wie Vignetten, Winterräder, Services, Reparaturen und am Ende müssen private von geschäftlichen Fahrten getrennt werden, damit die Steuern richtig bezahlt werden. Hier kommen wir ins Spiel.</p>
      <p>Wir übernehmen das Flottenmanagement für dein Unternehmen – entweder alles von A-Z oder individuell in einzelnen Modulen: Bedarfsanalyse, Beschaffung, Finanzierung, Betrieb, Rückgabe/Verkauf.</p>
    </div>
    <div class="panel" style="left:210px;top:252px;width:178px;height:200px">
      <h3>Transparent, das ist das Flottenmanagement der Solvara</h3>
      <p>Wir beraten dich in allen Fragen rund um die Mobilität. Du die Wahl, die Fahrzeuge selbst zu bezahlen oder uns die Finanzierung zu überlassen. Im Pannenfall, Service, Reifenwechsel sind wir für dich und deine Fahrer 7x24 erreichbar. Mit unserem Cockpit hast du jederzeit die Kosten deiner Flotte im Blick.</p>
      <h3>Intelligent vernetzt<br>dank Telematik</h3>
      <p>Du brauchst ein digitales Fahrtenbuch und möchtest zwischen beruflichen und privaten Fahrten unterscheiden? Du möchtest in Echtzeit wissen, wo deine Fahrzeuge sind und somit die Effizienz deiner Flotte steigern? Dank unserer Telematik-Lösungen ist das kein Problem.</p>
    </div>
    <div class="benefits" style="height:118px">
      <h4>Deine Vorteile auf einen Blick:</h4>
      <ul>
        <li>Eine Anlaufstelle für alle Anliegen – wir sind 365 Tage rund um die Uhr für dich da, auch im Ausland.</li>
        <li>Unsere erfahrenen Flottenmanager sind dein direkter Kontakt und kümmern sich um alles. Auch Schadenfälle werden durch sie erledigt.</li>
        <li>Sämtliche Kosten werden transparent ausgewiesen</li>
        <li>Fahrzeuge nach individuellen Bedürfnissen</li>
        <li>Solvara ist mit 1.1 Millionen versicherter Fahrzeuge ein etablierter Player im Markt</li>
        <li>Du profitierst von unserem Service-/Pannen und Reparaturnetzwerk</li>
      </ul>
    </div>
  </div>
</section>

</body>
</html>
```